Flyer Template

I need a flyer template for door knocking on properties. Text Boxes need to be editable, with a header and text body. Footer to be my info. Project to be stylized to match my real estate signs and logo art from past projects

```html
<!DOCTYPE html>
<html lang="en">
<head>
<meta charset="UTF-8">
<title>Door Knocking Flyer – Ardel Realty</title>
<link href="https://fonts.googleapis.com/css2?family=Arimo:wght@400;700&family=Cinzel:wght@700&family=Roboto+Condensed:wght@400;700&display=swap" rel="stylesheet">
<style>
  :root{
    --red:#e41e26;
    --black:#111111;
    --white:#ffffff;
    --text:#444444;
    --band-light:#f4f4f4;
    --band-mid:#dcdcdc;
    --stage:#4d4d4d;
  }
  *{margin:0;padding:0;box-sizing:border-box}
  html,body{width:1200px;height:1200px;overflow:hidden;background:var(--stage)}
  .canvas{position:relative;width:1200px;height:1200px}
  .flyer{position:absolute;left:196px;top:30px;width:807px;height:1140px;background:var(--white);overflow:hidden;box-shadow:0 6px 24px rgba(0,0,0,.35)}
  .photo{position:absolute;top:18px;width:248px;height:373px}
  .photo--house{left:16px;background:linear-gradient(180deg,#8f93c4 0%,#b3b3cf 45%,#6f7482 70%,#4f6b3c 88%,#6d6b70 100%)}
  .photo--walk{left:280px;background:linear-gradient(180deg,#9aa6a8 0%,#6f7f8e 35%,#46505a 65%,#8a8a86 100%)}
  .photo--door{left:543px;background:linear-gradient(90deg,#d8d8d8 0%,#f2f2f2 40%,#e6e6e6 70%,#2a2a2a 100%)}

  .brand{position:absolute;left:0;top:404px;width:153px;height:133px;display:flex;flex-direction:column;align-items:center;justify-content:flex-end;padding-bottom:2px}
  .brand__mark{width:40px;height:40px;background:var(--red);margin-bottom:22px}
  .brand__name{font-family:"Arimo",sans-serif;font-weight:700;font-size:21px;line-height:20px;color:var(--black);text-align:center;letter-spacing:.5px}

  .headline{position:absolute;left:153px;top:404px;width:638px;height:133px;background:linear-gradient(180deg,#e2e2e2 0%,#f7f7f7 45%,#dedede 100%);display:flex;flex-direction:column;align-items:center;justify-content:center;text-align:center;color:var(--red);font-family:"Cinzel",serif;font-weight:700}
  .headline__main{font-size:40px;line-height:44px}
  .headline__main small{font-size:20px}
  .headline__sub{font-size:20px;line-height:28px}
  .headline__sub b{font-size:25px}

  .intro{position:absolute;left:79px;top:566px;width:649px;height:108px}
  .intro__corner{position:absolute;width:112px;height:85px;border:3px solid var(--red)}
  .intro__corner--tl{left:0;top:0;border-right:none;border-bottom:none}
  .intro__corner--br{right:0;bottom:0;border-left:none;border-top:none}
  .intro__text{position:absolute;left:20px;right:20px;top:18px;font-family:"Arimo",sans-serif;font-size:19.5px;line-height:27.5px;color:var(--text);text-align:center}

  .feature-photo{position:absolute;left:42px;top:712px;width:248px;height:209px;background:linear-gradient(135deg,#c98a54 0%,#b8764a 45%,#d39a6a 70%,#e7d1bd 100%)}

  .feature{position:absolute;left:324px;top:709px;width:440px}
  .feature__title{font-family:"Cinzel",serif;font-weight:700;font-size:20px;color:var(--red);padding-bottom:2px;border-bottom:2px solid #cfcfcf;display:inline-block}
  .feature__list{list-style:none;margin-top:16px}
  .feature__list li{position:relative;padding-left:19px;font-family:"Arimo",sans-serif;font-size:15.2px;line-height:29.6px;color:var(--text)}
  .feature__list li::before{content:"";position:absolute;left:5px;top:11px;width:7px;height:7px;background:var(--red)}

  .agent{position:absolute;left:0;top:968px;width:807px;height:40px;display:flex;align-items:center;justify-content:center;gap:22px;background:linear-gradient(90deg,#fff 0%,#f0f0f0 50%,#fff 100%)}
  .agent__rule{width:88px;height:2px;background:var(--red)}
  .agent__name{font-family:"Roboto Condensed",sans-serif;font-weight:700;font-size:31px;color:var(--red);letter-spacing:.5px}

  .contact{position:absolute;left:0;top:1008px;width:807px;height:44px;background:linear-gradient(180deg,#e6e6e6,#d9d9d9);display:flex;align-items:center;justify-content:center;gap:30px;font-family:"Roboto Condensed",sans-serif;font-size:22px;color:#222}
  .contact__item{display:flex;align-items:center;gap:10px}
  .contact__item svg{fill:var(--red)}

  .footer{position:absolute;left:0;top:1052px;width:807px;height:88px;display:flex}
  .footer__office{width:320px;background:var(--black);display:flex;flex-direction:column;justify-content:center;padding-left:44px;color:var(--white)}
  .footer__office-name{font-family:"Roboto Condensed",sans-serif;font-weight:700;font-size:25px;line-height:26px}
  .footer__office-line{font-family:"Roboto Condensed",sans-serif;font-size:10px;letter-spacing:2px;margin-top:2px}
  .footer__notice{flex:1;margin-left:3px;background:var(--red);color:var(--white);display:flex;flex-direction:column;align-items:center;justify-content:center;font-family:"Roboto Condensed",sans-serif;text-align:center}
  .footer__notice-main{font-weight:700;font-size:22px;letter-spacing:1px;line-height:24px}
  .footer__notice-sub{font-size:17.5px;letter-spacing:1.5px;line-height:20px}
</style>
</head>
<body>
<div class="canvas">
  <article class="flyer">
    <div class="photo photo--house" role="img" aria-label="Two-storey family house with garage at dusk"></div>
    <div class="photo photo--walk" role="img" aria-label="Agent with briefcase walking up to a front door"></div>
    <div class="photo photo--door" role="img" aria-label="Agent in a suit knocking on a white door"></div>

    <div class="brand">
      <div class="brand__mark"></div>
      <div class="brand__name">ARDEL<br>REALTY</div>
    </div>

    <header class="headline">
      <div class="headline__main">Lorem Ipsum Dolor <small>sit</small></div>
      <div class="headline__sub">amet, consectetuer <b>Adipiscing Elit</b></div>
    </header>

    <section class="intro">
      <span class="intro__corner intro__corner--tl"></span>
      <span class="intro__corner intro__corner--br"></span>
      <p class="intro__text">Lorem ipsum dolor sit amet, consectetuer adipiscing elit, sed diam nonummy nibh euismod tincidunt ut laoreet dolore magna aliquam erat volutpat. Ut wisi enim ad minim veniam,</p>
    </section>

    <div class="feature-photo" role="img" aria-label="Hand holding a small model house in front of a brick wall"></div>

    <section class="feature">
      <h2 class="feature__title">Lorem ipsum dolor sit amet,</h2>
      <ul class="feature__list">
        <li>Lorem ipsum dolor sit amet, consectetuer adipiscing elit,</li>
        <li>Lorem ipsum dolor sit amet, consectetuer adipiscing elit,</li>
        <li>Lorem ipsum dolor sit amet, consectetuer adipiscing elit,</li>
        <li>Lorem ipsum dolor sit amet, consectetuer adipiscing elit,</li>
        <li>Lorem ipsum dolor sit amet, consectetuer adipiscing elit,</li>
        <li>Lorem ipsum dolor sit amet, consectetuer adipiscing elit,</li>
      </ul>
    </section>

    <div class="agent">
      <span class="agent__rule"></span>
      <span class="agent__name">MORGAN ARDEL</span>
      <span class="agent__rule"></span>
    </div>

    <div class="contact">
      <span class="contact__item">
        <svg width="22" height="22" viewBox="0 0 24 24" aria-hidden="true"><path d="M6.6 10.8a15.1 15.1 0 0 0 6.6 6.6l2.2-2.2c.3-.3.7-.4 1-.2 1.1.4 2.3.6 3.6.6.6 0 1 .4 1 1V20c0 .6-.4 1-1 1A17 17 0 0 1 3 4c0-.6.4-1 1-1h3.5c.6 0 1 .4 1 1 0 1.3.2 2.5.6 3.6.1.3 0 .7-.2 1z"/></svg>
        555-014-0277
      </span>
      <span class="contact__item">
        <svg width="26" height="18" viewBox="0 0 26 18" aria-hidden="true"><path d="M0 0h26v2L13 10 0 2z"/><path d="M0 4l13 8 13-8v14H0z"/></svg>
        mardel@example.com
      </span>
    </div>

    <footer class="footer">
      <div class="footer__office">
        <div class="footer__office-name">NORTH RIDGE GROUP</div>
        <div class="footer__office-line">NORTHRIDGEREALTY</div>
      </div>
      <div class="footer__notice">
        <div class="footer__notice-main">EACH OFFICE INDEPENDENTLY</div>
        <div class="footer__notice-sub">OWNED AND OPERATED</div>
      </div>
    </footer>
  </article>
</div>
</body>
</html>
```